Electrical panel service sticker w Bucket truck & Logo

We have a rather plain sticker we put on lighting panels to remind customers who to call for service. We want to redesign them with brushed aluminum background. We want a remake of the sticker with the outline of a bucket truck. You'll need to find or draw the outling of a bucket truck maybe with the boom up slightly as we will get these stickers die cut.

We want LOGO with Ph.# and Email.
Electrical * Lighting * Sign Service

Target Market(s)

Commercial property managers

Industry/Entity Type

Property Management

Requirements
Must have
• Bucket Truck Outline

```html
<!DOCTYPE html>
<html lang="en">
<head>
<meta charset="utf-8">
<title>Brightline Upkeep – Panel Service Sticker</title>
<link href="https://fonts.googleapis.com/css2?family=Montserrat:wght@500;600;800;900&display=swap" rel="stylesheet">
<style>
  :root {
    --page-bg: #e9e9e9;
    --brand-red: #ec1f27;
    --ink: #111111;
    --white: #ffffff;
    --alu-light: #f2f2f2;
    --alu-mid: #cfcfcf;
    --alu-dark: #b9b9b9;
    --black-top: #2a2a2a;
    --black-bottom: #0c0c0c;
    --truck-tone: #3a3a3a;
  }
  * { margin: 0; padding: 0; box-sizing: border-box; }
  html, body {
    width: 1200px;
    height: 900px;
    overflow: hidden;
    background: var(--page-bg);
  }
  .sticker {
    position: absolute;
    left: 40px;
    top: 124px;
    width: 1120px;
    height: 652px;
    overflow: hidden;
    box-shadow: 0 6px 18px rgba(0,0,0,0.25);
  }
  .brand-band {
    position: absolute;
    left: 0; top: 0;
    width: 1120px;
    height: 345px;
    background: linear-gradient(100deg, var(--alu-mid) 0%, var(--alu-light) 35%, var(--alu-dark) 55%, var(--alu-light) 80%, var(--alu-mid) 100%);
  }
  .brand-dot {
    position: absolute;
    left: 140px;
    top: 82px;
    width: 180px;
    height: 180px;
    border-radius: 50%;
    background: var(--brand-red);
  }
  .brand-name {
    position: absolute;
    left: 362px;
    top: 70px;
    font-family: "Montserrat", sans-serif;
    font-weight: 900;
    color: var(--brand-red);
    line-height: 1;
  }
  .brand-name .line-one {
    display: block;
    font-size: 82px;
    letter-spacing: 1px;
  }
  .brand-name .line-two {
    display: block;
    margin-top: 14px;
    font-size: 70px;
    letter-spacing: 8px;
  }
  .service-line {
    position: absolute;
    left: 364px;
    top: 240px;
    font-family: "Montserrat", sans-serif;
    font-weight: 800;
    font-size: 22px;
    letter-spacing: 1px;
    color: var(--brand-red);
    white-space: nowrap;
  }
  .legal-form {
    position: absolute;
    left: 528px;
    width: 260px;
    top: 296px;
    text-align: center;
    font-family: "Montserrat", sans-serif;
    font-weight: 500;
    font-size: 19px;
    letter-spacing: 2px;
    color: var(--ink);
  }
  .contact-band {
    position: absolute;
    left: 0; top: 345px;
    width: 1120px;
    height: 307px;
    background: linear-gradient(180deg, var(--black-top) 0%, var(--black-bottom) 100%);
  }
  .contact-row {
    position: absolute;
    left: 51px;
    display: flex;
    align-items: center;
    gap: 24px;
  }
  .contact-row.phone { top: 97px; }
  .contact-row.email { top: 177px; }
  .contact-icon {
    width: 50px;
    height: 50px;
    border-radius: 50%;
    background: var(--brand-red);
    display: flex;
    align-items: center;
    justify-content: center;
    flex: none;
  }
  .phone-number {
    font-family: "Montserrat", sans-serif;
    font-weight: 600;
    font-size: 58px;
    color: var(--brand-red);
    line-height: 1;
  }
  .email-address {
    font-family: "Montserrat", sans-serif;
    font-weight: 500;
    font-size: 32px;
    color: var(--white);
    line-height: 1;
    white-space: nowrap;
  }
  .truck-art {
    position: absolute;
    left: 741px;
    top: 20px;
    width: 360px;
    height: 234px;
    background: linear-gradient(180deg, var(--truck-tone), #222222);
  }
</style>
</head>
<body>
  <main class="sticker">
    <section class="brand-band">
      <div class="brand-dot"></div>
      <h1 class="brand-name">
        <span class="line-one">BRIGHTLINE</span>
        <span class="line-two">UPKEEP</span>
      </h1>
      <p class="service-line">ELECTRICAL • LIGHTING • SIGN SERVICE</p>
      <p class="legal-form">INCORPORATED</p>
    </section>

    <section class="contact-band">
      <div class="contact-row phone">
        <span class="contact-icon">
          <svg width="28" height="28" viewBox="0 0 24 24" aria-hidden="true">
            <path fill="#ffffff" d="M6.6 10.8a15.1 15.1 0 0 0 6.6 6.6l2.2-2.2a1 1 0 0 1 1-.25 11.4 11.4 0 0 0 3.6.57 1 1 0 0 1 1 1V20a1 1 0 0 1-1 1A17 17 0 0 1 3 4a1 1 0 0 1 1-1h3.5a1 1 0 0 1 1 1c0 1.25.2 2.45.57 3.57a1 1 0 0 1-.25 1z"/>
          </svg>
        </span>
        <span class="phone-number">877-555-0142</span>
      </div>
      <div class="contact-row email">
        <span class="contact-icon">
          <svg width="28" height="22" viewBox="0 0 28 22" aria-hidden="true">
            <rect x="1" y="2" width="26" height="18" rx="2" fill="#ffffff"/>
            <path d="M2 3 L14 13 L26 3" fill="none" stroke="#ec1f27" stroke-width="2"/>
          </svg>
        </span>
        <span class="email-address">service@brightlineupkeep.com</span>
      </div>
      <div class="truck-art" role="img" aria-label="White outline drawing of a utility bucket truck with its boom raised"></div>
    </section>
  </main>
</body>
</html>
```